Label for packages of Pure Raw Natural Honeycomb

This is a label that will be used to sell pure raw honeycomb on the internet and in farm gate sales
Label must contain my Logo (which is attached)
my website www.hivelanterngold.ca
the weight 300 gr and the words Pure Raw Honeycomb
label design should fit onto a sticker 3" by 2" oval but If the size appears to small to get all that info on I am willing to look at a different size or shape

Target Market(s)

internet and in person farm gate customers

Industry/Entity Type

Agriculture

Font styles to use
Other font styles liked:
• the font should compliment my logo font

Colors
ffc214

Requirements
Must have
• Label must contain my Logo (attached) my website www.hivelanterngold.ca
• the weight 300 gr and the words Pure Raw Honeycomb would like something in black and gold with a bit of an Elegant vintage feel
Nice to have
• vintage feel
• If the size appears to small to get all that info on I am willing to look at a different size or shape
Should not have
• no cartoons

```html
<!DOCTYPE html>
<html lang="en">
<head>
<meta charset="utf-8">
<title>Pure Raw Honeycomb Label</title>
<link rel="stylesheet" href="https://fonts.googleapis.com/css2?family=Arimo:wght@400;700&family=Playball&family=Great+Vibes&display=swap">
<style>
  :root {
    --backdrop: #ececec;
    --label-black: #050505;
    --comb-dark: #1c1c1c;
    --comb-mid: #2e2e2e;
    --gold: #ffc214;
    --lemon: #f2ea3a;
    --gold-deep: #e2a90a;
    --ink-white: #ffffff;
  }
  html, body {
    margin: 0;
    padding: 0;
    width: 1200px;
    height: 1147px;
    overflow: hidden;
    background: radial-gradient(ellipse at 50% 40%, #f7f7f7 0%, var(--backdrop) 70%, #dcdcdc 100%);
  }
  .canvas {
    position: relative;
    width: 1200px;
    height: 1147px;
  }
  .label {
    position: absolute;
    left: 93px;
    top: 60px;
    width: 1014px;
    height: 1027px;
  }
  .brand-name {
    font-family: "Arimo", Arial, sans-serif;
    font-weight: 700;
    fill: var(--ink-white);
  }
  .title-pure-raw {
    font-family: "Playball", cursive;
    fill: url(#lemonText);
  }
  .title-honeycomb {
    font-family: "Great Vibes", cursive;
    fill: var(--label-black);
  }
  .website, .weight {
    font-family: "Arimo", Arial, sans-serif;
    fill: var(--ink-white);
  }
</style>
</head>
<body>
<div class="canvas">
  <svg class="label" viewBox="0 0 780 790" xmlns="http://www.w3.org/2000/svg">
    <defs>
      <linearGradient id="lemonText" x1="0" y1="0" x2="0" y2="1">
        <stop offset="0" stop-color="#fbf46a"/>
        <stop offset="0.6" stop-color="#e8dc18"/>
        <stop offset="1" stop-color="#c9b10c"/>
      </linearGradient>
      <linearGradient id="ribbonGold" x1="0" y1="0" x2="1" y2="0">
        <stop offset="0" stop-color="var(--gold-deep)"/>
        <stop offset="0.3" stop-color="var(--lemon)"/>
        <stop offset="0.55" stop-color="var(--gold)"/>
        <stop offset="0.8" stop-color="var(--lemon)"/>
        <stop offset="1" stop-color="var(--gold-deep)"/>
      </linearGradient>
      <linearGradient id="tailGold" x1="0" y1="0" x2="0" y2="1">
        <stop offset="0" stop-color="var(--lemon)"/>
        <stop offset="1" stop-color="var(--gold)"/>
      </linearGradient>
      <radialGradient id="combTone" cx="0.5" cy="0.5" r="0.7">
        <stop offset="0" stop-color="var(--comb-mid)"/>
        <stop offset="1" stop-color="var(--comb-dark)"/>
      </radialGradient>
      <path id="tagShape" d="M100 130 H175 V70 H250 Q392 -10 535 70 H610 V130 H685 V660 H610 V720 H535 Q392 800 250 720 H175 V660 H100 Z"/>
    </defs>

    <!-- label body -->
    <use href="#tagShape" class="tag-outer" fill="var(--label-black)"/>
    <use href="#tagShape" class="tag-gold-frame" fill="none" stroke="var(--lemon)" stroke-width="11"
         transform="translate(392.5 395) scale(0.955 0.962) translate(-392.5 -395)"/>
    <use href="#tagShape" class="tag-inner-line" fill="none" stroke="var(--label-black)" stroke-width="4"
         transform="translate(392.5 395) scale(0.925 0.935) translate(-392.5 -395)"/>
    <path class="comb-pattern" role="img" aria-label="Faint honeycomb cells with honey bees"
          d="M140 165 H215 V110 H270 Q392 45 515 110 H570 V165 H645 V625 H570 V680 H515 Q392 745 270 680 H215 V625 H140 Z"
          fill="url(#combTone)" opacity="0.9"/>

    <!-- brand -->
    <circle class="brand-dot" cx="392" cy="130" r="14" fill="none" stroke="var(--ink-white)" stroke-width="4"/>
    <text class="brand-name" x="392" y="200" text-anchor="middle" font-size="38">Hive Lantern Gold</text>

    <!-- title -->
    <text class="title-pure-raw" x="398" y="365" text-anchor="middle" font-size="128">Pure Raw</text>

    <!-- ribbon -->
    <polygon class="ribbon-tail" points="0,478 96,440 112,548 28,590 60,530" fill="url(#tailGold)"/>
    <polygon class="ribbon-tail" points="776,478 690,440 672,548 758,590 726,530" fill="url(#tailGold)"/>
    <path class="ribbon-band" d="M88 462 Q392 395 698 432 L688 548 Q392 520 102 560 Z" fill="url(#ribbonGold)"/>
    <text class="title-honeycomb" x="395" y="525" text-anchor="middle" font-size="120" letter-spacing="4">Honeycomb</text>

    <!-- details -->
    <text class="website" x="392" y="640" text-anchor="middle" font-size="29">www.hivelanterngold.ca</text>
    <text class="weight" x="392" y="716" text-anchor="middle" font-size="33" transform="translate(392 0) scale(0.82 1) translate(-392 0)">weight:300 gr</text>
  </svg>
</div>
</body>
</html>
```